Radiant Crossing - An Exciting Mission & Book Cover Project

Help me to inspire people to live their best life! This is a mission, not just a design project.
I need a Book Cover designed to keep me inspired on the process of writing my book.
Book Title: Radiant Crossing
Tag Line: Three Simple Steps to get out of your own way, SuperCharge your Life and Step into Purpose!
Author: Marlis Quenby

The three steps are: Ownership, Vision and Action (Not sure if this should be on the front or back of the book cover)

The book is a self-help, motivational book. Personal development.
The cover needs to be strong and capture peoples attention, especially with competing shelf space. I almost see a fire ball of flame or explosion that will grab peoples attention.
My company is The Lantern Institute. I have added the company logo and a few pages of my presentation and topic outline to give an idea.
Maybe: The Lantern Institute logo on back of the cover. website is marlisquenby.com

THOUGHT: People should be able to take a photo of them holding the book cover showing what area of life they want Radiant Crossing in. This is why the front cover must be so visual and powerful that they want to take a photo with it. Ie. Explosion, fire, strong and bold.

Target Market(s)

Anyone who feels stuck and needs to breakthrough and move forward in life.

Industry/Entity Type

Motivation

Font styles to use
Serif
Sans Serif

Colors
ec1f27
f37122
fbed22

Requirements
Must have
• The design must be STRONG, SIMPLE, STAND OUT ON BOOK SHELVES.
Must have an open file to swap the photo and copy out.

Back Cover Page
1) Summary
2) 2-3 testimonials. One sentence.
3) About the Author (maybe with photo)
4) Lantern Institute logo
5) Website: radiantcrossing.com and marlisquenby.com
Nice to have
• If my photo works somewhere that would be great. I will change the photo later.
Added Where's Your Harbor? a nice cover example.
Should not have
• Right now I am writing the summary for the back of the cover. For now use Loreum Ipsum text and 2-3 recommendations. Again, I will get these only later.

```html
<!DOCTYPE html>
<html lang="en">
<head>
<meta charset="utf-8">
<title>Radiant Crossing – Cover Spread</title>
<link href="https://fonts.googleapis.com/css2?family=Archivo:wght@400;500;700;800;900&family=Oswald:wght@600;700&display=swap" rel="stylesheet">
<style>
  :root {
    --yellow: #fbed22;
    --ink: #0d0d0d;
    --paper: #ffffff;
    --photo-dark: #2a2d45;
    --photo-light: #c9a48a;
    --flame: #f37122;
  }
  * { margin: 0; padding: 0; box-sizing: border-box; }
  html, body {
    width: 1200px; height: 1165px; overflow: hidden;
    background: var(--paper);
    font-family: "Archivo", Arial, sans-serif;
    color: var(--ink);
  }
  .spread {
    position: absolute; left: 48px; top: 82px;
    width: 1104px; height: 1000px;
    display: flex;
  }

  /* ---------- Back cover ---------- */
  .back-cover {
    position: relative; width: 520px; height: 1000px;
    background: var(--yellow); overflow: hidden;
  }
  .back-title {
    position: absolute; left: 34px; top: 40px;
    font-size: 47px; font-weight: 800; letter-spacing: -1px; line-height: 1;
  }
  .back-rule { position: absolute; left: 34px; right: 0; height: 3px; background: var(--ink); }
  .back-tagline {
    position: absolute; left: 36px; top: 104px; right: 8px;
    font-size: 8.6px; text-transform: uppercase; letter-spacing: 0; white-space: nowrap;
  }
  .back-summary {
    position: absolute; left: 34px; top: 130px; width: 470px;
    font-size: 10.4px; line-height: 1.3; text-align: justify;
  }
  .course-heading {
    position: absolute; left: 34px; right: 0; top: 258px;
    text-align: center; font-size: 40px; font-weight: 800; letter-spacing: -0.8px;
  }
  .course-columns {
    position: absolute; left: 34px; top: 338px; width: 486px;
    display: grid; grid-template-columns: 1fr 1fr 1fr; column-gap: 10px;
  }
  .key { text-align: center; }
  .key-number { font-size: 15px; font-weight: 700; text-transform: uppercase; line-height: 1; }
  .key-name { font-size: 27px; font-weight: 800; text-transform: uppercase; line-height: 1.1; margin-bottom: 14px; }
  .key-list { list-style: none; }
  .key-list li { margin-bottom: 9px; line-height: 1.2; }
  .item-title { display: block; font-size: 6.6px; font-weight: 800; text-transform: uppercase; }
  .item-note { display: block; font-size: 5.8px; text-transform: uppercase; }

  .author-photo {
    position: absolute; left: 0; top: 702px; width: 196px; height: 298px;
    background: linear-gradient(180deg, var(--photo-light) 0%, var(--photo-light) 45%, var(--photo-dark) 60%, var(--photo-dark) 100%);
  }
  .author-name {
    position: absolute; left: 208px; top: 716px;
    font-size: 27px; font-weight: 800; letter-spacing: -0.4px;
  }
  .author-bio {
    position: absolute; left: 208px; top: 752px; width: 302px;
    font-size: 10.4px; line-height: 1.32; text-align: justify;
  }
  .websites {
    position: absolute; left: 262px; top: 900px;
    font-size: 10.4px; line-height: 1.4;
  }
  .imprint {
    position: absolute; left: 262px; top: 940px;
    display: flex; align-items: center; gap: 7px;
    font-size: 11px; font-weight: 800; text-transform: uppercase;
  }
  .imprint-dot { width: 12px; height: 12px; border-radius: 50%; background: var(--flame); }
  .back-footer { position: absolute; left: 0; right: 0; bottom: 0; height: 32px; background: var(--ink); }

  /* ---------- Spine ---------- */
  .spine {
    position: relative; width: 64px; height: 1000px; background: var(--ink);
  }
  .spine-text {
    position: absolute; left: 50%; top: 60px;
    transform: translateX(-50%);
    writing-mode: vertical-rl;
    color: var(--yellow); font-size: 34px; font-weight: 800; letter-spacing: -0.5px; white-space: nowrap;
  }
  .spine-divider { font-weight: 400; padding: 10px 0; }

  /* ---------- Front cover ---------- */
  .front-cover {
    position: relative; width: 520px; height: 1000px;
    background: var(--yellow); overflow: hidden;
  }
  .front-author {
    position: absolute; left: 0; right: 0; top: 48px; text-align: center;
    font-size: 54px; font-weight: 800; letter-spacing: -1px;
  }
  .title-band {
    position: absolute; background: var(--ink); color: var(--yellow);
    font-weight: 800; line-height: 1; white-space: nowrap;
  }
  .title-band--first {
    left: 30px; top: 140px; width: 470px; height: 155px;
    transform: rotate(2deg); font-size: 112px; letter-spacing: -3px;
    padding: 18px 0 0 22px;
  }
  .title-band--second {
    left: 36px; top: 306px; width: 460px; height: 110px;
    transform: rotate(1.2deg); font-size: 78px; letter-spacing: -1.5px;
    padding: 14px 0 0 32px;
  }
  .feature-art {
    position: absolute; left: 98px; top: 440px; width: 360px; height: 520px;
    background: var(--ink); border-radius: 44% 44% 46% 46% / 30% 30% 42% 42%;
  }
  .front-tagline {
    position: absolute; left: 110px; top: 600px; width: 330px;
    text-align: center; color: var(--yellow);
    font-family: "Oswald", "Archivo", sans-serif; font-weight: 700;
    font-size: 34px; line-height: 1.32; text-transform: uppercase;
  }
  .front-footer { position: absolute; left: 0; right: 0; bottom: 0; height: 40px; background: var(--ink); }
</style>
</head>
<body>
<main class="spread">

  <section class="back-cover">
    <h2 class="back-title">Radiant Crossing</h2>
    <div class="back-rule" style="top:94px"></div>
    <p class="back-tagline">Three simple steps to get out of your own way, supercharge your life and step into purpose</p>
    <p class="back-summary">Lorem ipsum dolor sit amet, consectetur adipisicing elit, sed do eiusmod tempor incididunt ut labore et dolore magna aliqua. Ut enim ad minim veniam, quis nostrud exercitation ullamco laboris nisi ut aliquip ex ea commodo consequat. Duis aute irure dolor in reprehenderit in voluptate velit esse cillum dolore eu fugiat nulla pariatur. Excepteur sint occaecat cupidatat non proident, sunt in culpa qui officia deserunt mollit anim id est laborum. Sed ut perspiciatis unde omnis iste natus error sit voluptatem accusantium doloremque laudantium, totam rem aperiam, eaque ipsa quae ab illo inventore veritatis et quasi arc.</p>
    <div class="back-rule" style="top:238px"></div>
    <h3 class="course-heading">Course Content</h3>
    <div class="back-rule" style="top:312px"></div>

    <div class="course-columns">
      <div class="key">
        <div class="key-number">First Key</div>
        <div class="key-name">Ownership</div>
        <ul class="key-list">
          <li><span class="item-title">Embracing your journey</span><span class="item-note">100% ownership + radical acceptance</span></li>
          <li><span class="item-title">The perfect experience you needed to have</span><span class="item-note">in order to wake up</span></li>
          <li><span class="item-title">Growth through pain &amp; challenge</span><span class="item-note">finding purpose in pain</span></li>
          <li><span class="item-title">Letting go of toxic emotions</span><span class="item-note">anger, resentment, guilt, shame, jealousy</span></li>
          <li><span class="item-title">Shifting from victim to victor</span><span class="item-note">choosing healthy emotions</span></li>
          <li><span class="item-title">Reframing your story</span><span class="item-note">shaping an empowered narrative</span></li>
          <li><span class="item-title">Breaking up with the idea of perfection</span><span class="item-note">because it doesn't exist</span></li>
        </ul>
      </div>
      <div class="key">
        <div class="key-number">Second Key</div>
        <div class="key-name">Vision</div>
        <ul class="key-list">
          <li><span class="item-title">The power of vision</span><span class="item-note">the secret jet fuel of action</span></li>
          <li><span class="item-title">Being authentic to yourself</span><span class="item-note">it's your life, not anyone else's</span></li>
          <li><span class="item-title">Crafting your 10-year goal</span><span class="item-note">starting with the end in mind</span></li>
          <li><span class="item-title">Chunking down</span><span class="item-note">short + medium term goals</span></li>
          <li><span class="item-title">Future pacing</span><span class="item-note">experience your nirvana right now</span></li>
          <li><span class="item-title">How your goal serves others</span><span class="item-note">our ultimate purpose</span></li>
          <li><span class="item-title">Constant realignment</span><span class="item-note">tweaking our goals as we go</span></li>
        </ul>
      </div>
      <div class="key">
        <div class="key-number">Third Key</div>
        <div class="key-name">Action</div>
        <ul class="key-list">
          <li><span class="item-title">Blocks to taking action</span><span class="item-note">fear, procrastination &amp; people</span></li>
          <li><span class="item-title">Small steps daily</span><span class="item-note">the power of consistency &amp; persistence</span></li>
          <li><span class="item-title">Comfort vs. calling</span><span class="item-note">doing things you don't want to</span></li>
          <li><span class="item-title">Showing up with excellence</span><span class="item-note">habits of peak performers</span></li>
          <li><span class="item-title">VIP support structure</span><span class="item-note">mentors &amp; building a team</span></li>
          <li><span class="item-title">Grit &amp; resilience</span><span class="item-note">dealing with 'no'</span></li>
          <li><span class="item-title">Constant daily growth</span><span class="item-note">growth through what you go through</span></li>
        </ul>
      </div>
    </div>

    <div class="back-rule" style="top:690px"></div>
    <div class="author-photo" role="img" aria-label="Portrait photograph of the author in a dark blazer"></div>
    <h3 class="author-name">Marlis Quenby</h3>
    <p class="author-bio">Lorem ipsum dolor sit amet, consectetur adipisicing elit, sed do eiusmod tempor incididunt ut labore et dolore magna aliqua. Ut enim ad minim veniam, quis nostrud exercitation ullamco laboris nisi ut aliquip ex ea commodo consequat. Duis aute dolor in reprehenderit in voluptate velit esse cillum dolore eu fugiat nulla pariatur. Excepteur sint occaecat cupidatat non proident, sunt in culpa qui officia deserunt anim id est laborum. Sed ut perspiciatis unde omnis iste natus error sit voluptatem.</p>
    <p class="websites">radiantcrossing.com<br>and marlisquenby.com</p>
    <div class="imprint"><span class="imprint-dot"></span>The Lantern Institute</div>
    <div class="back-footer"></div>
  </section>

  <section class="spine">
    <div class="spine-text">Radiant Crossing <span class="spine-divider">|</span> Marlis Quenby</div>
  </section>

  <section class="front-cover">
    <h2 class="front-author">Marlis Quenby</h2>
    <h1>
      <span class="title-band title-band--first">Radiant</span>
      <span class="title-band title-band--second">Crossing</span>
    </h1>
    <div class="feature-art" role="img" aria-label="Black silhouette illustration of a hand grenade"></div>
    <p class="front-tagline">Three simple steps to get out of your own way, supercharge your life and step into purpose!</p>
    <div class="front-footer"></div>
  </section>

</main>
</body>
</html>
```